Clinic for cellulit and fat removal

Name of clinic :
Lumera
- Body & Health (this has to be written on the site.)
I need CMS for me to be able to make changes myself.
A webpage for woman searching for a solution to remove fat and cellulit.
The owner is a brazilian woman in Denmark, and want her sense of aestetic shines thru the website.
There needs to be a slide show on the landing page showing big sliding pictures, of the clinic and and the treatments.
The Cryolipolysis, is a treatment freezing fat and cellulit, and this treatment will be the Attraction of the clinic.
Needs These pages in a horisontal fasion. (written in Danish)
Lumera
Behandlinger
- Cryolipolysis
- Silkora
- Lymfemassage
- Tandrelia
- Copper Tide
Produkter
Priser
Kontakt

```html
<!DOCTYPE html>
<html lang="en">
<head>
<meta charset="utf-8">
<title>Lumera – Body &amp; Health</title>
<link href="https://fonts.googleapis.com/css2?family=Montserrat:wght@300;400;500;600;700;800&family=Open+Sans:wght@400;600&display=swap" rel="stylesheet">
<style>
:root{
  --teal:#5bbcc8;
  --teal-mid:#68c6d1;
  --teal-light:#7ad3dc;
  --ink:#333;
  --muted:#555;
  --grey-bg:#ebebed;
  --panel:#e5e5e7;
  --white:#fff;
  --line:#dadada;
}
*{margin:0;padding:0;box-sizing:border-box}
html,body{width:1200px;height:4554px;overflow:hidden;background:var(--white)}
body{font-family:"Open Sans",sans-serif;color:var(--ink)}
.page{position:relative;width:1200px;height:4554px;overflow:hidden}
.abs{position:absolute}
.btn{position:absolute;display:flex;align-items:center;justify-content:center;background:var(--teal);color:#fff;font-family:"Montserrat",sans-serif;font-weight:600;font-size:13px;letter-spacing:.3px;text-transform:uppercase}
.btn-outline{background:#fff;color:var(--teal)}
.heading{position:absolute;left:0;width:1200px;text-align:center;font-family:"Montserrat",sans-serif;font-weight:600;color:var(--teal);font-size:28px;letter-spacing:.3px}
.fill{position:absolute}

/* header */
.brand{font-family:"Montserrat",sans-serif;font-weight:300;color:var(--teal);letter-spacing:2px}
.top-book{left:532px;top:23px;width:284px;height:30px;font-size:12px;font-weight:500;text-transform:uppercase;gap:8px}
.lang{position:absolute;top:23px;width:70px;height:30px;border:1px solid var(--line);font-size:10px;color:#666;display:flex;align-items:center;justify-content:center;gap:6px}
.flag{width:12px;height:8px;background:#c8102e}
.search{position:absolute;left:1039px;top:23px;width:28px;height:28px;background:var(--teal)}
.nav{position:absolute;top:78px;font-family:"Montserrat",sans-serif;font-size:11px;font-weight:500;color:#333;letter-spacing:.3px}

/* hero */
.hero{left:0;top:120px;width:1200px;height:608px;background:linear-gradient(100deg,#b8c1c5 0%,#d9dddf 35%,#c9b6a9 60%,#a8aaaf 100%)}
.hero-title{position:absolute;left:124px;top:360px;font-family:"Montserrat",sans-serif;font-weight:800;font-size:62px;line-height:70px;color:#fff;letter-spacing:1px}
.dot{position:absolute;top:666px;width:10px;height:10px;border-radius:50%;background:#fff}

/* info band */
.band{position:absolute;top:728px;height:186px}
.band h4{position:absolute;top:764px;font-family:"Montserrat",sans-serif;font-weight:600;font-size:14px;color:#fff}
.band-text{position:absolute;top:794px;font-size:14px;color:#fff}
.band .btn{top:841px;height:34px}

/* welcome */
.card{position:absolute;background:#fff;box-shadow:0 3px 12px rgba(0,0,0,.15)}
.para{font-size:15px;line-height:30px;color:#444}

/* testimonial */
.tcard{position:absolute;top:2622px;width:442px;height:295px;border:1px solid var(--line);background:#fff}
.quote{position:absolute;left:26px;top:12px;font-family:Georgia,serif;font-size:90px;color:#cfcfcf;line-height:1}
.ttext{position:absolute;left:74px;top:66px;width:330px;font-size:14px;line-height:26px;color:#444}
.avatar{position:absolute;left:74px;top:192px;width:60px;height:60px;border-radius:50%;background:linear-gradient(#9aa0a6,#5d6166)}
.tname{position:absolute;left:150px;top:212px;font-family:"Montserrat",sans-serif;font-weight:600;font-size:11px;color:#333}
.tloc{position:absolute;left:150px;top:232px;font-size:10px;color:#777}

/* cellulit */
.tick{position:absolute;left:139px;width:16px;height:16px}
.bullet{position:absolute;left:175px;width:420px;font-size:14px;line-height:27px;color:#444}

/* news */
.ncard{position:absolute;top:3714px;width:283px;height:368px;border:1px solid var(--line);background:#fff}
.nimg{position:absolute;left:0;top:0;width:281px;height:174px}
.ncap{position:absolute;left:18px;top:160px;width:245px;height:60px;background:#fff}
.ntitle{position:absolute;left:36px;top:170px;width:220px;font-size:15px;line-height:23px;color:#222}
.ntext{position:absolute;left:36px;top:234px;width:220px;font-size:10.5px;line-height:19px;color:#555}
.ncard .btn{left:36px;top:312px;width:96px;height:29px;font-size:11px}

/* footer */
.footer{position:absolute;left:0;top:4135px;width:1200px;height:419px;background:#f1f1f3}
.ftitle{position:absolute;top:4192px;font-family:"Montserrat",sans-serif;font-weight:600;font-size:11px;color:var(--teal);letter-spacing:.3px}
.ftext{position:absolute;font-size:11px;line-height:21px;color:#444}
.social{position:absolute;top:4483px;width:22px;height:22px}
</style>
</head>
<body>
<div class="page">

  <!-- header -->
  <div class="abs brand" style="left:128px;top:30px;font-size:54px;line-height:62px">LUMERA</div>
  <div class="btn top-book">
    <svg width="12" height="12" viewBox="0 0 24 24"><path fill="#fff" d="M6.6 10.8a15.1 15.1 0 0 0 6.6 6.6l2.2-2.2c.3-.3.7-.4 1-.2 1.1.4 2.3.6 3.6.6.6 0 1 .4 1 1V20c0 .6-.4 1-1 1A17 17 0 0 1 3 4c0-.6.4-1 1-1h3.5c.6 0 1 .4 1 1 0 1.3.2 2.5.6 3.6.1.3 0 .7-.2 1z"/></svg>
    <span>Book appointment <span style="font-size:15px">(555).014.2290</span></span>
  </div>
  <div class="lang" style="left:868px"><span class="flag"></span>Danish</div>
  <div class="lang" style="left:951px"><span class="flag" style="background:#1f3d8c"></span>English</div>
  <div class="search">
    <svg width="28" height="28" viewBox="0 0 28 28"><circle cx="13" cy="13" r="5" fill="none" stroke="#fff" stroke-width="2"/><path d="M17 17l4 4" stroke="#fff" stroke-width="2"/></svg>
  </div>
  <div class="nav" style="left:531px">LUMERA</div>
  <div class="nav" style="left:631px">BEHANDLINGER
    <svg width="12" height="8" viewBox="0 0 12 8" style="margin-left:12px"><path d="M1 1l5 5 5-5" stroke="#5bbcc8" stroke-width="1.8" fill="none"/></svg></div>
  <div class="nav" style="left:800px">PRODUKTER</div>
  <div class="nav" style="left:926px">PRISER</div>
  <div class="nav" style="left:1012px">KONTAKT</div>
  <div class="abs" style="left:0;top:119px;width:1200px;height:1px;background:#e6e6e6"></div>

  <!-- hero -->
  <div class="fill hero" role="img" aria-label="Slideshow photo of a slim woman measuring her waist with a tape measure"></div>
  <div class="hero-title">BODY &amp;<br>HEALTH</div>
  <div class="btn" style="left:129px;top:527px;width:322px;height:60px;font-size:15px;box-shadow:0 3px 8px rgba(0,0,0,.2)">Book a consultation today</div>
  <div class="dot" style="left:544px"></div>
  <div class="dot" style="left:569px;background:none;border:2px solid var(--teal);width:12px;height:12px;top:665px"></div>
  <div class="dot" style="left:597px"></div>
  <div class="dot" style="left:621px"></div>
  <div class="dot" style="left:645px"></div>

  <!-- info band -->
  <div class="band" style="left:0;width:399px;background:var(--teal)"></div>
  <div class="band" style="left:399px;width:401px;background:var(--teal-mid)"></div>
  <div class="band" style="left:800px;width:400px;background:var(--teal-light)"></div>

  <svg class="abs" style="left:42px;top:770px" width="50" height="50" viewBox="0 0 50 50"><circle cx="25" cy="25" r="22" fill="none" stroke="#fff" stroke-width="4"/><path d="M25 13v13h-8" stroke="#fff" stroke-width="4" fill="none"/></svg>
  <div class="band"><h4 style="left:131px">OPENING TIMES:</h4></div>
  <div class="band-text" style="left:131px">Mon - Fri 8 - 8, Sat 9 - 5</div>
  <div class="band"><div class="btn btn-outline" style="left:131px;width:134px">Call us now</div></div>

  <svg class="abs" style="left:438px;top:766px" width="44" height="46" viewBox="0 0 44 46"><rect x="2" y="6" width="40" height="38" fill="none" stroke="#fff" stroke-width="3"/><rect x="2" y="6" width="40" height="9" fill="#fff"/><path d="M11 1v9M33 1v9" stroke="#fff" stroke-width="3"/><g fill="#fff"><rect x="8" y="20" width="6" height="5"/><rect x="19" y="20" width="6" height="5"/><rect x="30" y="20" width="6" height="5"/><rect x="8" y="29" width="6" height="5"/><rect x="19" y="29" width="6" height="5"/><rect x="30" y="29" width="6" height="5"/><rect x="8" y="37" width="6" height="4"/><rect x="19" y="37" width="6" height="4"/></g></svg>
  <div class="band"><h4 style="left:517px">BOOK APPOINTMENTS</h4></div>
  <div class="band-text" style="left:517px">But I must explain to you how</div>
  <div class="band"><div class="btn btn-outline" style="left:517px;width:136px">Book now</div></div>

  <svg class="abs" style="left:840px;top:766px" width="46" height="44" viewBox="0 0 46 44"><rect x="3" y="14" width="40" height="9" fill="#fff"/><rect x="6" y="25" width="34" height="18" fill="#fff"/><rect x="21" y="14" width="4" height="29" fill="#7ad3dc"/><path d="M23 14c-4-10-14-10-12-3 1 2 6 3 12 3zM23 14c4-10 14-10 12-3-1 2-6 3-12 3z" fill="#fff"/></svg>
  <div class="band"><h4 style="left:910px">SPECIAL OFFERS</h4></div>
  <div class="band-text" style="left:910px">Find out this months' seasonal offer!</div>
  <div class="band"><div class="btn btn-outline" style="left:910px;width:134px">Find out now</div></div>

  <!-- welcome -->
  <div class="card" style="left:258px;top:914px;width:684px;height:394px"></div>
  <div class="heading" style="top:965px;font-size:14px;font-weight:500">WELCOME TO</div>
  <div class="heading brand" style="top:995px;font-size:60px;font-weight:300;letter-spacing:2px">LUMERA</div>
  <div class="abs para" style="left:300px;top:1091px;width:600px;text-align:center">There are many variations of passages of Lorem Ipsum available, but the majority have suffered alteration in some form &nbsp;by injected humour, or randomised words which don't.</div>
  <div class="btn" style="left:535px;top:1217px;width:129px;height:37px">Read more</div>

  <!-- what is -->
  <div class="heading" style="top:1372px">WHAT IS LUMERA?</div>
  <div class="fill" style="left:132px;top:1460px;width:518px;height:424px;background:radial-gradient(ellipse at 50% 45%,#d8b8a6 0%,#b69484 45%,#4a4a4d 90%)" role="img" aria-label="Video still of a woman pinching belly fat"></div>
  <div class="abs" style="left:342px;top:1630px;width:96px;height:62px;background:rgba(91,188,200,.85)"></div>
  <svg class="abs" style="left:377px;top:1647px" width="28" height="28" viewBox="0 0 28 28"><path d="M3 2l22 12L3 26z" fill="#fff"/></svg>
  <div class="abs" style="left:650px;top:1460px;width:417px;height:424px;background:var(--panel)"></div>
  <div class="abs" style="left:703px;top:1500px;width:330px;font-size:24px;line-height:35px;color:var(--teal)">It is a long established fact reader will be distracted by readable content</div>
  <div class="abs" style="left:703px;top:1627px;width:318px;font-size:13px;line-height:26.5px;color:#444;text-align:justify">There are many variations of passages of Lorem Ipsum available, but the majority have suffered alteration in some form, by injected humour, or randomised words which don't look even slightly believable.</div>
  <div class="btn" style="left:705px;top:1797px;width:131px;height:36px">Read more</div>

  <!-- before & after -->
  <div class="abs" style="left:0;top:1953px;width:1200px;height:498px;background:var(--grey-bg)"></div>
  <div class="fill" style="left:0;top:1953px;width:503px;height:498px;background:linear-gradient(90deg,#d9c2b4 0%,#e9d8cd 45%,#3e5a7a 85%,#ebebed 100%)" role="img" aria-label="Woman's waist marked with liposuction guide arrows, wearing loose jeans"></div>
  <div class="abs" style="left:507px;top:2012px;font-family:Montserrat,sans-serif;font-weight:600;font-size:28px;color:var(--teal)">BEFORE &amp; AFTER PHOTOS</div>
  <div class="fill" style="left:511px;top:2085px;width:182px;height:103px;background:linear-gradient(90deg,#d8b3a0 50%,#e8a3b8 50%)" role="img" aria-label="Before and after photo of hips in bikini"></div>
  <div class="fill" style="left:703px;top:2085px;width:181px;height:103px;background:linear-gradient(90deg,#e9c2ae 50%,#efc9b6 50%)" role="img" aria-label="Before and after photo of buttocks"></div>
  <div class="fill" style="left:894px;top:2085px;width:182px;height:103px;background:linear-gradient(90deg,#eeeeee 50%,#f4f4f4 50%)" role="img" aria-label="Before and after photo of torso in white shirt"></div>
  <div class="fill" style="left:511px;top:2202px;width:182px;height:102px;background:linear-gradient(90deg,#d5a88f 50%,#dfb39a 50%)" role="img" aria-label="Before and after photo of upper body"></div>
  <div class="fill" style="left:703px;top:2202px;width:181px;height:102px;background:linear-gradient(90deg,#e3c3b2 50%,#eacdbd 50%)" role="img" aria-label="Before and after photo of waist"></div>
  <div class="fill" style="left:894px;top:2202px;width:182px;height:102px;background:linear-gradient(180deg,#2b2b30 40%,#d9b39f 40%,#d9b39f 70%,#7d9ab8 70%)" role="img" aria-label="Before and after photo of stomach above jeans"></div>
  <div class="abs" style="left:514px;top:2336px;width:9px;height:9px;border-radius:50%;background:#c4c4c4"></div>
  <div class="abs" style="left:536px;top:2336px;width:9px;height:9px;border-radius:50%;background:#c4c4c4"></div>
  <div class="abs" style="left:557px;top:2335px;width:11px;height:11px;border-radius:50%;background:var(--teal)"></div>
  <div class="abs" style="left:580px;top:2336px;width:9px;height:9px;border-radius:50%;background:#c4c4c4"></div>
  <div class="abs" style="left:602px;top:2336px;width:9px;height:9px;border-radius:50%;background:#c4c4c4"></div>
  <div class="abs" style="left:624px;top:2336px;width:9px;height:9px;border-radius:50%;background:#c4c4c4"></div>
  <div class="btn" style="left:922px;top:2338px;width:154px;height:32px;font-size:11px">View more photos</div>

  <!-- testimonials -->
  <div class="heading" style="top:2522px">CLIENT TESTIMONIALS</div>
  <svg class="abs" style="left:64px;top:2748px" width="20" height="36" viewBox="0 0 20 36"><path d="M17 2L3 18l14 16" stroke="#999" stroke-width="3" fill="none"/></svg>
  <svg class="abs" style="left:1114px;top:2748px" width="20" height="36" viewBox="0 0 20 36"><path d="M3 2l14 16L3 34" stroke="#999" stroke-width="3" fill="none"/></svg>
  <div class="tcard" style="left:132px">
    <div class="quote">&ldquo;</div>
    <div class="ttext">There are many variations of passages of Lorem Ipsum available, but the majority have suffered alteration in some form, by injected humour, or randomised.</div>
    <div class="avatar" role="img" aria-label="Client portrait"></div>
    <div class="tname">MARTA HOLM</div><div class="tloc">England</div>
  </div>
  <div class="tcard" style="left:627px">
    <div class="quote">&ldquo;</div>
    <div class="ttext">There are many variations of passages of Lorem Ipsum available, but the majority have suffered alteration in some form, by injected humour, or randomised.</div>
    <div class="avatar" role="img" aria-label="Client portrait"></div>
    <div class="tname">MARTA HOLM</div><div class="tloc">England</div>
  </div>

  <!-- cellulit -->
  <div class="abs" style="left:0;top:3004px;width:1200px;height:539px;background:var(--grey-bg)"></div>
  <div class="fill" style="left:512px;top:3004px;width:601px;height:539px;background:radial-gradient(ellipse at 60% 55%,#f0d9cb 0%,#e7cbbb 30%,#ebebed 68%)" role="img" aria-label="Woman with smooth legs sitting on the floor"></div>
  <div class="abs" style="left:136px;top:3056px;font-family:Montserrat,sans-serif;font-weight:600;font-size:28px;color:var(--teal)">CELLULIT</div>
  <div class="abs" style="left:136px;top:3101px;width:520px;font-size:22px;line-height:35px;color:#333">It is a long established fact &nbsp;reader will be distracted by readable content</div>
  <svg class="tick" style="top:3210px" viewBox="0 0 16 16"><circle cx="8" cy="8" r="8" fill="var(--teal)"/><path d="M4.5 8.2l2.3 2.3 4.5-4.6" stroke="#fff" stroke-width="1.8" fill="none"/></svg>
  <div class="bullet" style="top:3204px">There are many variations of passages of Lorem Ipsum</div>
  <svg class="tick" style="top:3265px" viewBox="0 0 16 16"><circle cx="8" cy="8" r="8" fill="var(--teal)"/><path d="M4.5 8.2l2.3 2.3 4.5-4.6" stroke="#fff" stroke-width="1.8" fill="none"/></svg>
  <div class="bullet" style="top:3259px">At vero eos et accusamus et iusto odio dignissimos ducimus qui blanditiis praesentium</div>
  <svg class="tick" style="top:3344px" viewBox="0 0 16 16"><circle cx="8" cy="8" r="8" fill="var(--teal)"/><path d="M4.5 8.2l2.3 2.3 4.5-4.6" stroke="#fff" stroke-width="1.8" fill="none"/></svg>
  <div class="bullet" style="top:3338px">On the other hand, we denounce with righteous indignation and dislike</div>
  <div class="btn" style="left:143px;top:3440px;width:131px;height:36px">Read more</div>

  <!-- news -->
  <svg class="abs" style="left:454px;top:3615px" width="16" height="30" viewBox="0 0 16 30"><path d="M14 2L3 15l11 13" stroke="#999" stroke-width="2.5" fill="none"/></svg>
  <div class="heading" style="top:3613px">LATEST NEWS</div>
  <svg class="abs" style="left:716px;top:3615px" width="16" height="30" viewBox="0 0 16 30"><path d="M2 2l11 13L2 28" stroke="#999" stroke-width="2.5" fill="none"/></svg>

  <div class="ncard" style="left:157px">
    <div class="nimg" role="img" aria-label="Waist wrapped with a yellow tape measure" style="background:linear-gradient(160deg,#c99a86,#e3c0ad 60%,#d2b09e)"></div>
    <div class="ncap"></div>
    <div class="ntitle">There are many variations of passages of Lorem</div>
    <div class="ntext">But I must explain to you how all this mistaken idea of denouncing pleasure and praising pain was born</div>
    <div class="btn">Read more</div>
  </div>
  <div class="ncard" style="left:461px">
    <div class="nimg" role="img" aria-label="Torso of a person opening a shirt" style="background:linear-gradient(90deg,#aeb5c3,#cfb09f 45%,#cfb09f 55%,#aeb5c3)"></div>
    <div class="ncap"></div>
    <div class="ntitle">At vero eos et accusamus et iusto odio dignissimos</div>
    <div class="ntext">These cases are perfectly simple and easy to distinguish &nbsp;In a free hour, when our power of choice is .</div>
    <div class="btn">Read more</div>
  </div>
  <div class="ncard" style="left:763px">
    <div class="nimg" role="img" aria-label="Hands pinching belly fat above checked trousers" style="background:linear-gradient(180deg,#3c4f7a 0%,#c69d88 40%,#d9b6a3 100%)"></div>
    <div class="ncap"></div>
    <div class="ntitle">On the other hand, we denounce with righteous</div>
    <div class="ntext">he rejects pleasures to secure other greater pleasures, or else he endures pains to avoid.</div>
    <div class="btn">Read more</div>
  </div>

  <!-- footer -->
  <div class="footer"></div>
  <div class="abs brand" style="left:134px;top:4256px;font-size:54px;line-height:62px">LUMERA</div>

  <div class="ftitle" style="left:435px">CONTACT US</div>
  <svg class="abs" style="left:439px;top:4244px" width="10" height="13" viewBox="0 0 10 13"><path d="M5 0a5 5 0 0 1 5 5c0 3-5 8-5 8S0 8 0 5a5 5 0 0 1 5-5z" fill="#555"/><circle cx="5" cy="5" r="1.8" fill="#f1f1f3"/></svg>
  <div class="ftext" style="left:472px;top:4238px">27 Linden Walk<br>Aarhus, 8000</div>
  <svg class="abs" style="left:438px;top:4302px" width="12" height="12" viewBox="0 0 24 24"><path fill="#555" d="M6.6 10.8a15.1 15.1 0 0 0 6.6 6.6l2.2-2.2c.3-.3.7-.4 1-.2 1.1.4 2.3.6 3.6.6.6 0 1 .4 1 1V20c0 .6-.4 1-1 1A17 17 0 0 1 3 4c0-.6.4-1 1-1h3.5c.6 0 1 .4 1 1 0 1.3.2 2.5.6 3.6.1.3 0 .7-.2 1z"/></svg>
  <div class="ftext" style="left:472px;top:4298px">555.014.2290</div>
  <svg class="abs" style="left:437px;top:4347px" width="13" height="10" viewBox="0 0 13 10"><rect x=".5" y=".5" width="12" height="9" fill="none" stroke="#555"/><path d="M.5.5l6 5 6-5" fill="none" stroke="#555"/></svg>
  <div class="ftext" style="left:472px;top:4342px">info@lumera.dk</div>

  <div class="ftitle" style="left:677px">MENU</div>
  <div class="ftext" style="left:677px;top:4234px">Lumera<br>Behandlinger<br>Produkter<br>Priser<br>Kontakt</div>

  <div class="ftitle" style="left:832px">NEWSLETTER SIGNUP!</div>
  <div class="abs" style="left:832px;top:4241px;width:235px;height:42px;background:#fff;border:1px solid var(--line)"></div>
  <svg class="abs" style="left:851px;top:4257px" width="12" height="9" viewBox="0 0 13 10"><rect x=".5" y=".5" width="12" height="9" fill="none" stroke="#555"/><path d="M.5.5l6 5 6-5" fill="none" stroke="#555"/></svg>
  <div class="ftext" style="left:882px;top:4252px;font-size:10px">E mail id</div>
  <div class="btn" style="left:975px;top:4302px;width:92px;height:32px;font-size:13px">Signup!</div>

  <div class="abs" style="left:132px;top:4439px;width:935px;height:1px;background:#d6d6d6"></div>
  <div class="abs" style="left:131px;top:4488px;font-family:Montserrat,sans-serif;font-weight:600;font-size:9px;color:var(--teal)">FOLLOW US</div>
  <div class="social" style="left:212px;background:#3b5998"></div>
  <div class="social" style="left:240px;background:#3fa9e0"></div>
  <div class="social" style="left:268px;background:#dd4b39"></div>
  <div class="social" style="left:296px;background:#0e76a8"></div>
  <div class="ftext" style="left:867px;top:4482px;width:200px;text-align:right;font-size:10px">Copyrights @ 2017 All Rights Reserved</div>
</div>
</body>
</html>
```